Hvac service truck vinyl decals

2023 q480 RTV
You can find the logo i want to use at
kelmovent.com
Include
Logo
Don't Sweat, Call Kelmo!
Website
Ph# 9851937046

```html
<!DOCTYPE html>
<html lang="en">
<head>
<meta charset="utf-8">
<title>Kelmo Vent – Truck Wrap Concepts</title>
<link href="https://fonts.googleapis.com/css2?family=Montserrat:wght@500;700;800&family=Poppins:wght@500;600&display=swap" rel="stylesheet">
<style>
  :root {
    --wrap-red: #e0262c;
    --wrap-blue: #3d8fc6;
    --wrap-white: #ffffff;
    --body-grey: #eceef0;
    --body-line: #c9cdd2;
    --glass: #3a3f45;
    --tyre: #2a2d31;
    --rim: #a7adb3;
    --page: #ffffff;
  }
  html, body {
    margin: 0;
    padding: 0;
    width: 1200px;
    height: 1200px;
    overflow: hidden;
    background: var(--page);
  }
  .canvas {
    position: relative;
    width: 1200px;
    height: 1200px;
  }
  .concept {
    position: absolute;
    left: 100px;
    width: 1000px;
    height: 340px;
  }
  .concept--a { top: 190px; }
  .concept--b { top: 660px; }
  .brand-name {
    font-family: 'Montserrat', sans-serif;
    font-weight: 800;
    fill: var(--wrap-red);
  }
  .tagline {
    font-family: 'Poppins', sans-serif;
    font-weight: 500;
    fill: var(--wrap-white);
  }
  .tagline-accent {
    font-weight: 600;
    fill: var(--wrap-blue);
  }
  .phone {
    font-family: 'Montserrat', sans-serif;
    font-weight: 700;
    fill: var(--wrap-white);
    letter-spacing: 2px;
  }
  .website {
    font-family: 'Poppins', sans-serif;
    font-weight: 500;
    fill: var(--wrap-white);
    letter-spacing: 1px;
  }
  .service-badge {
    font-family: 'Montserrat', sans-serif;
    font-weight: 700;
    fill: var(--wrap-white);
  }
  .body-shape { fill: var(--body-grey); stroke: var(--body-line); stroke-width: 2; }
  .glass { fill: var(--glass); }
  .tyre { fill: var(--tyre); }
  .rim { fill: var(--rim); }
  .red { fill: var(--wrap-red); }
  .blue { fill: var(--wrap-blue); }
  .white { fill: var(--wrap-white); }
</style>
</head>
<body>
<main class="canvas">

  <!-- Concept A: angled stripes -->
  <svg class="concept concept--a" viewBox="0 0 1000 340" aria-label="Truck wrap concept with angled stripes">
    <g role="img" aria-label="Pickup truck side view">
      <path class="body-shape" d="M20 140 L40 115 L210 100 L330 25 L625 22 L630 110 L975 110 L980 265 L20 265 Z"/>
      <path class="glass" d="M270 100 L345 38 L470 36 L470 100 Z"/>
      <path class="glass" d="M485 36 L605 36 L608 100 L485 100 Z"/>
    </g>

    <path class="red" d="M240 225 L620 225 L660 160 L650 265 L240 265 Z"/>
    <path class="blue" d="M240 212 L610 212 L680 110 L700 110 L625 220 L240 220 Z"/>
    <path class="red" d="M680 110 L975 110 L975 205 L760 205 L720 265 L640 265 Z"/>
    <path class="blue" d="M775 215 L975 215 L975 262 L745 262 Z"/>

    <text class="tagline" x="725" y="140" font-size="17">Don't Sweat, <tspan class="tagline-accent">Call Kelmo!</tspan></text>
    <text class="phone" x="725" y="178" font-size="30">985.193.7046</text>
    <text class="service-badge" x="905" y="236" font-size="14">24/7</text>
    <text class="service-badge" x="890" y="248" font-size="9">Emergency</text>
    <text class="service-badge" x="898" y="258" font-size="9">Services</text>

    <circle class="red" cx="285" cy="165" r="14"/>
    <text class="brand-name" x="308" y="180" font-size="42">KELMO VENT</text>
    <text class="website" x="260" y="252" font-size="17">kelmovent.com</text>

    <circle class="tyre" cx="195" cy="272" r="62"/>
    <circle class="rim" cx="195" cy="272" r="34"/>
    <circle class="tyre" cx="810" cy="272" r="62"/>
    <circle class="rim" cx="810" cy="272" r="34"/>
  </svg>

  <!-- Concept B: rising sweep -->
  <svg class="concept concept--b" viewBox="0 0 1000 340" aria-label="Truck wrap concept with rising sweep">
    <g role="img" aria-label="Pickup truck side view">
      <path class="body-shape" d="M20 140 L40 115 L210 100 L330 25 L625 22 L630 110 L975 110 L980 265 L20 265 Z"/>
      <path class="glass" d="M270 100 L345 38 L470 36 L470 100 Z"/>
      <path class="glass" d="M485 36 L605 36 L608 100 L485 100 Z"/>
    </g>

    <path class="blue" d="M240 200 L640 200 L690 165 L705 165 L650 208 L240 208 Z"/>
    <path class="red" d="M240 222 L620 222 L700 175 L722 175 L645 265 L240 265 Z"/>
    <path class="red" d="M640 110 L975 110 L975 190 L700 190 Z"/>
    <path class="blue" d="M700 205 L975 205 L975 262 L660 262 Z"/>

    <text class="tagline" x="745" y="135" font-size="16">Don't Sweat, <tspan class="tagline-accent">Call Kelmo!</tspan></text>
    <text class="phone" x="745" y="170" font-size="28">985.193.7046</text>
    <text class="service-badge" x="905" y="234" font-size="14">24/7</text>
    <text class="service-badge" x="890" y="246" font-size="9">Emergency</text>
    <text class="service-badge" x="898" y="256" font-size="9">Services</text>

    <circle class="red" cx="275" cy="175" r="11"/>
    <text class="brand-name" x="293" y="186" font-size="30">KELMO VENT</text>
    <text class="website" x="260" y="252" font-size="17">kelmovent.com</text>

    <circle class="tyre" cx="195" cy="272" r="62"/>
    <circle class="rim" cx="195" cy="272" r="34"/>
    <circle class="tyre" cx="810" cy="272" r="62"/>
    <circle class="rim" cx="810" cy="272" r="34"/>
  </svg>

</main>
</body>
</html>
```